Stationery Design Project

We need a stationery design to change our look to a more corporate design. My company has been established since 1989 and over that time has changed from your average sign company to doing more Corporate re branding projects and have some multi National clients.
Our website is currently being redesigned so we need a new logo and business cards etc. to compliment it.
I have 2 graphic designers employed but i want on outsiders opinion and a totally independant view point.
Updates
Hi Designers
We are predominantely a sign manufacturing company that manufacturers every type of sign you can imagine. However the majoprity of our work is digital graphics. Our claim to faim is that we wrap the Harbour Skytrams and Glidetrams which everyone seems to know in Sydney.We also do all sorts of Large format digital printing, vehicle wraps,vinyl signage,LED & Neon Illuminated signage,CNC Routing all materials,Laser cutting and Engraving, Architectural signage, Cut Out letters and Screenprinting.
Aswell as this we totally re-brand companies with internal wall graphics reception signage way finding signage and the like.We are a medium size company that has been trading since 1989 and has some very large reputable clients.
Our Company name is Brightmark Pty Ltd but like to have Signage and Graphics in our stationery.
Our details are as follows T: 9381 5027 F: 9381 5063 Unit 4, 22 Quarry Lane.Pine Flats. NSW 2163 email mail@brightmarkexample.com our current website is being re-designed www.brightmarkexample.com
The design and colour scheme i would like is quite simple with a corporate feel and blue, grey & magenta are colours that seem to suit but am open to most suggestions just looking for clean lines.
Hopefully this is enough information if you require any more please ask.
Regards Neil Barrowby
We are looking to simplify our LOGO not too concerned yet about layout of stationery items that we can easily work on later. I want to get a new logo that we can work with before we return to work on the 16th January so please concentrate on just the logo for now.
We would like to have Signs & Graphics somewhere in the name even though our registered name is Brightmark Pty Ltd. Brightmark is one word, i want it to be quite a bold font with no seriffs.The bright blue and grey colours are favourites so far with maybe a little magenta added later. Would like to have a Logo that is totally seperate and then the Brightmark P/L Signs & graphics as a secondary item just to let people know what Brightmark do as the name obviously does not say what we are about.
Also we need to consider how we can put logo on T-shirts work shirts and company vehicles.
We do not need CD cover or envelopes but letterheads and business cards.
Industry/Entity Type
Business
Look and feel
Each slider illustrates characteristics of the customer's brand and the style your logo design should communicate.

```html
<!DOCTYPE html>
<html lang="en">
<head>
<meta charset="utf-8">
<title>Brightmark business card</title>
<link href="https://fonts.googleapis.com/css2?family=Open+Sans:wght@400;600;700&display=swap" rel="stylesheet">
<style>
  :root {
    --page: #e9ebee;
    --sky-deep: #0d63b0;
    --sky: #2f8fd8;
    --sky-light: #56c4f5;
    --band-warm: #f3c23a;
    --band-cool: #4cb6ea;
    --panel-warm: #cfdc4f;
    --panel-cool: #c4d6e0;
    --ink: #111111;
    --ink-soft: #8a8a8a;
    --white: #ffffff;
  }
  * { box-sizing: border-box; margin: 0; padding: 0; }
  html, body { width: 1200px; height: 900px; overflow: hidden; }
  body {
    background: var(--page);
    font-family: "Open Sans", Arial, sans-serif;
    position: relative;
  }
  .card {
    position: absolute;
    left: 240px;
    width: 720px;
    height: 404px;
    border-radius: 18px;
    overflow: hidden;
    box-shadow: 0 6px 18px rgba(0,0,0,0.18);
  }
  .card--front { top: 30px; background: linear-gradient(#ffffff, #ececec); }
  .card--back {
    top: 466px;
    background: radial-gradient(circle at 30% 30%, var(--sky-light) 0%, var(--sky) 55%, var(--sky-deep) 100%);
  }

  .card__sky {
    position: absolute; left: 0; top: 0; width: 100%; height: 150px;
    background: linear-gradient(var(--sky-deep), var(--sky));
  }
  .card__band {
    position: absolute; left: 0; top: 150px; width: 100%; height: 40px;
    background: linear-gradient(90deg, var(--band-warm), var(--band-cool) 50%, var(--band-warm));
    opacity: 0.85;
  }
  .card__panel {
    position: absolute; right: 60px; width: 230px; height: 150px;
    background: linear-gradient(90deg, var(--panel-warm), var(--panel-cool));
    opacity: 0.55;
  }
  .card__panel--top { top: 0; }
  .card__panel--bottom { bottom: 0; right: 150px; }

  .brand {
    position: absolute; color: var(--white); font-weight: 700;
    line-height: 1; letter-spacing: -0.5px;
  }
  .card--front .brand { left: 22px; top: 22px; font-size: 28px; }
  .card--back .brand { left: 66px; top: 160px; font-size: 64px; }

  .holder { position: absolute; right: 22px; top: 222px; text-align: right; }
  .holder__name { font-size: 22px; color: var(--ink); font-weight: 400; line-height: 1.15; }
  .holder__role { font-size: 16px; color: var(--ink-soft); font-weight: 600; line-height: 1.2; }

  .address { position: absolute; left: 22px; top: 282px; font-size: 19px; color: var(--ink-soft); line-height: 1.3; }
  .contact { position: absolute; left: 22px; top: 340px; display: flex; align-items: center; gap: 8px; font-size: 16px; color: var(--ink-soft); }
  .contact__fax { margin-left: 22px; }
  .contact svg { display: block; }
  .mail { position: absolute; left: 22px; top: 368px; font-size: 16px; color: var(--ink-soft); }
  .web { position: absolute; font-size: 16px; }
  .card--front .web { right: 22px; top: 368px; color: var(--ink); }
  .card--back .web { left: 24px; bottom: 20px; color: var(--white); }
</style>
</head>
<body>

<section class="card card--front" aria-label="Business card front">
  <div class="card__sky"></div>
  <div class="card__band" role="img" aria-label="Converging yellow, blue and orange stripe decoration"></div>

  <p class="brand">Brightmark</p>

  <div class="holder">
    <p class="holder__name">Martin Keogh</p>
    <p class="holder__role">Director</p>
  </div>

  <p class="address">Unit 6/18 Carver Street, Pine Flats<br>NSW 2163</p>

  <div class="contact">
    <svg width="24" height="24" viewBox="0 0 24 24" aria-label="Phone">
      <circle cx="12" cy="12" r="10.5" fill="none" stroke="#333" stroke-width="1.6"/>
      <path d="M8.2 6.5 l2 2.4 -1.2 1.4 c0.8 1.8 2 3 3.8 3.8 l1.4-1.2 2.4 2 -1.4 2 c-4 -0.4 -7.6 -4 -8 -8 z" fill="#333"/>
    </svg>
    <span>(02) 9381 5027</span>
    <svg class="contact__fax" width="28" height="22" viewBox="0 0 28 22" aria-label="Fax">
      <rect x="8" y="1" width="12" height="8" fill="#fff" stroke="#999"/>
      <rect x="2" y="8" width="24" height="10" rx="2" fill="#d8d8d8" stroke="#999"/>
      <rect x="6" y="14" width="16" height="6" fill="#fff" stroke="#999"/>
    </svg>
    <span>(02) 9381 5063</span>
  </div>
  <p class="mail">Mail - mail@brightmarkexample.com</p>
  <p class="web">www.brightmarkexample.com</p>
</section>

<section class="card card--back" aria-label="Business card back">
  <div class="card__panel card__panel--top" role="img" aria-label="Diagonal multi-colour bar decoration"></div>
  <div class="card__panel card__panel--bottom" role="img" aria-label="Diagonal multi-colour bar decoration"></div>

  <p class="brand">Brightmark</p>
  <p class="web">www.brightmarkexample.com</p>
</section>

</body>
</html>
```